Sticker Redesign

We provide document shredding services to clients. Clients are provided with shredding bins and employees/users of these companies dispose of unwanted confidential documents into these bins. Based on their schedule we come out and shred their documents in our specialty trucks and recycle the paper at the end of the day. We have our company decal on these bins which have a few objectives:
1. Motivate clients/users to dispose of all paper documents into our bins.
2. Instruct these clients/users on what can and CAN NOT go into our bins.
3. Brand our company
REDESIGN OBJECTIVES:
1. Our current label needs a redesign that will include items that cannot be placed into our bin as we have had an increase of items such as batteries and metal objects deposited into our bins. This leads to fires in our shredding trucks.
Allowed in Container: Paper Documents Only
Not Allowed in Container: All Other Waste; Batteries, Food, Metal, Electronics.
2. We also want to do a better job in educating clients/users to dispose of confidential documents into our bins and not garbage or recycling bins under their desks.
3. Modern, clean design look.
4. Size of label should remain the same.
Office employees

```html
<!DOCTYPE html>
<html lang="en">
<head>
<meta charset="utf-8">
<title>Clearleaf Shredding Bin Label</title>
<link rel="stylesheet" href="https://fonts.googleapis.com/css2?family=Montserrat:wght@600;700;800&family=Source+Sans+3:wght@400;600;700&display=swap">
<style>
  :root {
    --brand-blue: #1aa0dc;
    --ink: #1c1c1c;
    --paper: #ffffff;
    --backdrop: #e9eaec;
  }
  * { margin: 0; padding: 0; box-sizing: border-box; }
  html, body { width: 882px; height: 1200px; overflow: hidden; }
  body {
    background: var(--backdrop);
    display: flex;
    align-items: center;
    justify-content: center;
  }
  .bin-label {
    position: relative;
    width: 820px;
    height: 196px;
    background: var(--paper);
    overflow: hidden;
    box-shadow: 0 1px 3px rgba(0,0,0,0.12);
  }
  .instruction-band {
    position: absolute;
    inset: 0;
    background: var(--brand-blue);
    clip-path: polygon(0 0, 610px 0, 572px 100%, 0 100%);
    padding: 34px 0 0 40px;
    font-family: "Montserrat", sans-serif;
    color: var(--paper);
  }
  .security-note {
    color: var(--ink);
    font-size: 12px;
    font-weight: 700;
    line-height: 1.25;
    letter-spacing: 0.1px;
    text-transform: uppercase;
  }
  .band-rule {
    width: 480px;
    height: 2px;
    background: var(--paper);
    margin: 10px 0 12px -40px;
  }
  .allowed {
    font-size: 33px;
    font-weight: 800;
    line-height: 1;
    letter-spacing: 0.2px;
  }
  .not-allowed {
    display: flex;
    align-items: center;
    gap: 8px;
    margin-top: 4px;
  }
  .not-allowed-word {
    font-size: 38px;
    font-weight: 800;
    line-height: 1;
  }
  .not-allowed-list {
    font-size: 13.5px;
    font-weight: 700;
    line-height: 1.15;
    text-transform: uppercase;
  }
  .brand-panel {
    position: absolute;
    top: 0;
    right: 0;
    width: 230px;
    height: 100%;
    padding: 44px 24px 0 0;
    text-align: right;
    font-family: "Source Sans 3", sans-serif;
  }
  .brand-name {
    display: inline-flex;
    align-items: center;
    gap: 8px;
    color: var(--brand-blue);
    font-size: 36px;
    font-weight: 700;
    line-height: 1;
  }
  .brand-name::before {
    content: "";
    width: 12px;
    height: 12px;
    background: var(--brand-blue);
  }
  .brand-tagline {
    color: var(--ink);
    font-size: 18px;
    font-weight: 400;
    margin-top: 6px;
  }
  .brand-rule {
    height: 1.5px;
    background: var(--brand-blue);
    margin: 12px 0 6px 14px;
  }
  .brand-contact {
    color: var(--brand-blue);
    font-size: 12.5px;
    font-weight: 600;
  }
</style>
</head>
<body>
  <section class="bin-label">
    <div class="instruction-band">
      <p class="security-note">Confidential material should be disposed of in this bin.<br>Wastebaskets and recycling containers are not secure.</p>
      <div class="band-rule"></div>
      <p class="allowed">PAPER DOCUMENTS ONLY</p>
      <div class="not-allowed">
        <span class="not-allowed-word">NO</span>
        <span class="not-allowed-list">Batteries, food, metal, electronics or<br>other waste</span>
      </div>
    </div>
    <div class="brand-panel">
      <p class="brand-name">Clearleaf</p>
      <p class="brand-tagline">Information Security</p>
      <div class="brand-rule"></div>
      <p class="brand-contact">www.clearleaf-shred.ca &nbsp;|&nbsp; 800-555-0142</p>
    </div>
  </section>
</body>
</html>
```